Brevane Advisory business card

Premium business card required
I have attached the brand as a powerpoint template but this can be made to look very up market, I have also attached my BIO for title reasons and to give you a feel for my skills
front of card
Darrel Voskuij
Managing Director Brevane Advisory
Retail, Customer-Led Experience, Transformation and Maximising Shareholder Return
Mobile +61(0)487395028
Email darrelbrevaneadvisory.example
back of card

BREVANE ADVISORY’ OFFERING

We transform customer environments to extract benefits while elevating service levels;
We release millions of dollars in self-funding through continuous improvement;
We see CX as a key differentiator, proactively guarding share from market disrupters;
We re-invent service and create front-end of the future.

```html
<!DOCTYPE html>
<html lang="en">
<head>
<meta charset="utf-8">
<title>Brevane Advisory business card</title>
<link href="https://fonts.googleapis.com/css2?family=Roboto:wght@400;500;700&family=Roboto+Condensed:wght@700&display=swap" rel="stylesheet">
<style>
  :root {
    --backdrop: #262626;
    --paper: #f3f3f3;
    --band-grey: #4f4f4f;
    --gold: #c8a92c;
    --ink: #4a4a4a;
    --body-text: #555555;
    --watermark: #d9d9d9;
    --white: #ffffff;
  }
  * { box-sizing: border-box; margin: 0; padding: 0; }
  html, body { width: 1200px; height: 960px; overflow: hidden; }
  body {
    position: relative;
    background: var(--backdrop);
    font-family: "Roboto", Arial, sans-serif;
  }
  .card {
    position: absolute;
    width: 600px;
    height: 343px;
    background: var(--paper);
    overflow: hidden;
    box-shadow: 0 3px 8px rgba(0,0,0,.5);
  }
  .card--front { left: 314px; top: 113px; }
  .card--back { left: 311px; top: 472px; }

  /* front */
  .brand {
    position: absolute;
    left: 0; top: 0;
    width: 100%; height: 194px;
    display: flex; align-items: center; justify-content: center;
    gap: 14px;
  }
  .brand__name {
    font-weight: 700;
    font-size: 36px;
    letter-spacing: 1px;
    color: var(--ink);
  }
  .brand__dot {
    width: 42px; height: 42px;
    border-radius: 50%;
    background: var(--ink);
  }
  .identity {
    position: absolute;
    left: 0; top: 194px;
    width: 100%; height: 112px;
    background: var(--band-grey);
    text-align: center;
    color: var(--white);
    padding-top: 15px;
  }
  .identity__name {
    font-family: "Roboto Condensed", "Arial Narrow", sans-serif;
    font-weight: 700;
    font-size: 22px;
    color: var(--gold);
    text-transform: uppercase;
    line-height: 26px;
  }
  .identity__role {
    font-size: 14.5px;
    line-height: 18px;
  }
  .contact {
    position: absolute;
    left: 0; top: 306px;
    width: 100%; height: 37px;
    background: var(--gold);
    display: flex; align-items: center; justify-content: center;
    gap: 7px;
    padding: 0 12px;
    color: var(--white);
    font-size: 12.5px;
    white-space: nowrap;
  }
  .contact__item { display: flex; align-items: center; gap: 4px; }
  .contact__icon { fill: var(--white); flex: none; }

  /* back */
  .watermark-disc {
    position: absolute;
    left: 280px; top: 11px;
    width: 320px; height: 320px;
    border-radius: 50%;
    background: var(--watermark);
    opacity: .8;
  }
  .offering {
    position: absolute;
    left: 55px; top: 82px;
    width: 405px;
  }
  .offering__title {
    font-family: "Roboto Condensed", "Arial Narrow", sans-serif;
    font-weight: 700;
    font-size: 21px;
    color: var(--gold);
    text-transform: uppercase;
    margin-bottom: 14px;
  }
  .offering__list { list-style: none; }
  .offering__item {
    position: relative;
    padding-left: 20px;
    font-size: 14.5px;
    line-height: 17px;
    color: var(--body-text);
    margin-bottom: 8px;
  }
  .offering__item:last-child { margin-top: 12px; }
  .offering__item::before {
    content: "";
    position: absolute;
    left: 1px; top: 3px;
    width: 11px; height: 11px;
    border-radius: 50%;
    background: var(--body-text);
  }
</style>
</head>
<body>
  <section class="card card--front">
    <div class="brand">
      <span class="brand__name">BREVANE ADVISORY</span>
      <span class="brand__dot"></span>
    </div>
    <div class="identity">
      <h1 class="identity__name">Darrel Voskuij</h1>
      <p class="identity__role">Managing Director Brevane Advisory</p>
      <p class="identity__role">Retail, Customer-Led Experience</p>
      <p class="identity__role">Transformation &amp; Maximising Shareholder Return</p>
    </div>
    <div class="contact">
      <span class="contact__item">
        <svg class="contact__icon" width="9" height="15" viewBox="0 0 10 16"><path d="M1.5 0h7A1.5 1.5 0 0 1 10 1.5v13A1.5 1.5 0 0 1 8.5 16h-7A1.5 1.5 0 0 1 0 14.5v-13A1.5 1.5 0 0 1 1.5 0zM1.5 2v10.5h7V2zM5 13.3a.9.9 0 1 0 0 1.8.9.9 0 0 0 0-1.8z"/></svg>
        +61(0)487395028
      </span>
      <span class="contact__item">
        <svg class="contact__icon" width="13" height="9" viewBox="0 0 14 10"><path d="M0 0h14v1.2L7 5.6 0 1.2zM0 2.6l7 4.4 7-4.4V10H0z"/></svg>
        dv@darrelbrevaneadvisory.example
      </span>
      <span class="contact__item">
        <svg class="contact__icon" width="13" height="13" viewBox="0 0 14 14"><circle cx="7" cy="7" r="6" fill="none" stroke="#fff" stroke-width="1.6"/><path d="M3.5 4.5h3l1 2-1.5 1.5 1 2.5-2 1-1-3-1.5-1zM8.5 2.5l2.5 1.5-.5 2.5-2-1z"/></svg>
        darrelbrevaneadvisory.example
      </span>
    </div>
  </section>

  <section class="card card--back">
    <div class="watermark-disc"></div>
    <div class="offering">
      <h2 class="offering__title">Brevane Advisory’ Offering</h2>
      <ul class="offering__list">
        <li class="offering__item">We transform customer environments to extract benefits while elevating service levels;</li>
        <li class="offering__item">We release millions of dollars in self-funding through continuous improvement;</li>
        <li class="offering__item">We see CX as a key differentiator, proactively guarding share from market disrupters;</li>
        <li class="offering__item">We re-invent service and create front-end of the future.</li>
      </ul>
    </div>
  </section>
</body>
</html>
```